Zielgruppe
Endkunde ist eine Immobilienfirma ((Bauträger)
Aufgabenstellung
Das Design soll für eine Präsentationsmappe erstellt werden und die Bemaßung sowie Farbigleit der vorgegebnen pdf-Datei beinhalten. Es soll in den Hausfarben , nebst den Backround in grau, gehalten werden.

```html
<!DOCTYPE html>
<html lang="de">
<head>
<meta charset="utf-8">
<title>Präsentationsmappe – Wohnwerk Elbland AG</title>
<link rel="stylesheet" href="https://fonts.googleapis.com/css2?family=Noto+Serif:wght@400;700&family=Crimson+Text&display=swap">
<style>
  :root{
    --paper:#c8c8c8;
    --paper-light:#d3d3d3;
    --brand-red:#8e2a25;
    --text-grey:#4a4a4a;
    --guide-blue:#5bc8e8;
    --die-pink:#e0507a;
    --rule:#222;
  }
  html,body{margin:0;padding:0;overflow:hidden;background:var(--paper);}
  .sheet{position:relative;width:1200px;height:883px;background:var(--paper);overflow:hidden;
    font-family:"Noto Serif",Georgia,serif;}
  .light-band{position:absolute;left:0;top:77px;width:1200px;height:100px;background:var(--paper-light);}
  .fold-line{position:absolute;left:0;top:264px;width:1200px;height:1px;background:var(--rule);}
  .photo{position:absolute;}
  .photo--team{left:151px;top:4px;width:513px;height:260px;
    background:linear-gradient(180deg,#f4f3f1 0%,#ebe6e1 18%,#e2c3aa 38%,#d8b489 52%,#b49a80 64%,#6e625a 80%,#3c3532 100%);}
  .photo--office{left:676px;top:264px;width:319px;height:476px;
    background:linear-gradient(220deg,#f2f2f2 0%,#d6d6d6 20%,#9a9a9a 42%,#6f6f6f 60%,#4b4b4b 80%,#2e2e2e 100%);}
  .photo--sketch{left:1005px;top:264px;width:195px;height:242px;
    background:linear-gradient(180deg,#f1f1f1 0%,#e6e6e6 55%,#dadada 100%);}
  .photo--townhouses{left:1005px;top:514px;width:195px;height:226px;
    background:linear-gradient(180deg,#da4c4f 0%,#d65a5b 30%,#e7a09e 50%,#d47a78 65%,#a4262b 82%,#7d1519 100%);}
  .accent-rule{position:absolute;left:797px;top:193px;width:403px;height:5px;background:var(--brand-red);}
  .brand{position:absolute;display:flex;align-items:center;gap:6px;color:var(--brand-red);}
  .brand__name{text-align:right;line-height:1.05;font-weight:400;}
  .brand__mark{background:var(--brand-red);flex:none;}
  .brand--cover{right:168px;top:122px;font-size:20px;}
  .brand--cover .brand__mark{width:34px;height:34px;}
  .brand--front{right:684px;top:532px;font-size:20px;}
  .brand--front .brand__mark{width:34px;height:34px;}
  .brand--spine{right:1081px;top:288px;font-size:9px;}
  .brand--spine .brand__mark{width:14px;height:14px;}
  .headline{position:absolute;left:151px;width:513px;top:276px;margin:0;text-align:center;
    font-weight:700;font-size:18.5px;color:var(--brand-red);}
  .contact{position:absolute;text-align:right;font-family:"Crimson Text",Georgia,serif;color:var(--text-grey);margin:0;}
  .contact .label{color:var(--brand-red);}
  .contact--front{right:743px;top:586px;font-size:10.5px;line-height:12px;}
  .contact--front .gap{height:6px;}
  .contact--spine{right:1081px;top:319px;font-size:8.5px;line-height:10px;}
  .contact--spine .gap{height:10px;}
  .web-band{position:absolute;height:24px;background:var(--brand-red);color:#fff;
    font-family:"Crimson Text",Georgia,serif;font-size:12px;letter-spacing:4px;
    display:flex;align-items:center;justify-content:center;}
  .web-band--front{left:0;top:682px;width:664px;}
  .web-band--front span{margin-left:151px;}
  .web-band--back{left:676px;top:682px;width:234px;}
  .web-band--flap{left:146px;top:766px;width:518px;transform:rotate(180deg);}
  .guides{position:absolute;left:0;top:0;}
</style>
</head>
<body>
<div class="sheet">
  <div class="light-band"></div>

  <div class="photo photo--team" role="img" aria-label="Foto: fröhliches Team mit erhobenen Daumen"></div>
  <div class="fold-line"></div>

  <div class="brand brand--cover">
    <div class="brand__name">Wohnwerk<br>Elbland AG</div>
    <div class="brand__mark"></div>
  </div>
  <div class="accent-rule"></div>

  <div class="photo photo--office" role="img" aria-label="Schwarzweißfoto: modernes Bürogebäude mit Baum"></div>
  <div class="photo photo--sketch" role="img" aria-label="Architekturskizze eines Neubaus"></div>
  <div class="photo photo--townhouses" role="img" aria-label="Rot getöntes Foto: Altbau-Häuserzeile"></div>

  <div class="brand brand--spine">
    <div class="brand__name">Wohnwerk<br>Elbland AG</div>
    <div class="brand__mark"></div>
  </div>
  <div class="contact contact--spine">
    Lindenhofweg 12<br>01468 Talheim<br><span class="label">FON</span> 03 51 / 48 26 11 70
    <div class="gap"></div>
    Birkenallee 7<br>89520 Auenfeld<br><span class="label">FON</span> 0 73 21 / 55 40 82
    <div class="gap"></div>
    <span class="label">E-MAIL</span> kontakt@wwe-ag.de
  </div>

  <h1 class="headline">Ihre Zufriedenheit, ist unsere Motivation!</h1>

  <div class="brand brand--front">
    <div class="brand__name">Wohnwerk<br>Elbland AG</div>
    <div class="brand__mark"></div>
  </div>
  <div class="contact contact--front">
    Lindenhofweg 12<br>01468 Talheim
    <div class="gap"></div>
    <span class="label">FON</span> 03 51 / 48 26 11 70<br>
    <span class="label">FAX</span> 03 51 / 48 26 11 71
    <div class="gap"></div>
    <span class="label">E-MAIL</span> kontakt@wwe-ag.de
  </div>

  <div class="web-band web-band--front"><span>www.wwe-ag.de</span></div>
  <div class="web-band web-band--back">www.wwe-ag.de</div>
  <div class="web-band web-band--flap">www.wwe-ag.de</div>

  <svg class="guides" width="1200" height="883" viewBox="0 0 1200 883" aria-hidden="true">
    <g stroke="var(--guide-blue)" stroke-width="0.7" fill="none">
      <line x1="139" y1="12" x2="139" y2="728"/>
      <line x1="151" y1="4" x2="151" y2="730"/>
      <line x1="663" y1="4" x2="663" y2="730"/>
      <line x1="676" y1="12" x2="676" y2="730"/>
      <line x1="151" y1="730" x2="663" y2="730"/>
      <line x1="151" y1="742" x2="663" y2="742"/>
    </g>
    <g stroke="var(--die-pink)" stroke-width="0.7" fill="none" stroke-dasharray="4 3">
      <line x1="139" y1="12" x2="1188" y2="12"/>
      <line x1="1188" y1="12" x2="1188" y2="730"/>
      <line x1="676" y1="730" x2="1188" y2="730"/>
      <path d="M139 12 L30 38 Q12 45 12 62 L12 688 Q12 702 28 707 L139 728"/>
      <path d="M151 742 L186 776 Q168 800 170 830 Q180 862 220 860 Q240 856 246 845 L276 870 L620 870 Q640 868 646 840 L663 730"/>
      <path d="M482 755 a10 10 0 0 0 20 0"/>
      <path d="M612 797 a12 12 0 0 0 0 24"/>
    </g>
    <path d="M40 622 L40 635 L98 693 L110 693" stroke="var(--die-pink)" stroke-width="0.7" fill="none"/>
  </svg>
</div>
</body>
</html>
```